ASSET BASED PROGRAM FLIER

Need flier to market hard money loan products offered HARD MONEY FIX & FLIP PROGRAMS

We offer a variety of loan programs Some program highlights include......

1) No Minimum Credit Score
2) 3-5 Day Close
3) Up to 100% of Purchase & Rehab
4) Rates as Low as 7%
5) Loans Offered Nationwide

Contact us today for more information at (800) 647-2915 x42 or email us at mwelton@brightlanefunding.example NMLS #731856 www.brightlanefunding.example

```html
<!DOCTYPE html>
<html lang="en">
<head>
<meta charset="utf-8">
<title>Hard Money Fix &amp; Flip Programs Flier</title>
<link rel="stylesheet" href="https://fonts.googleapis.com/css2?family=Open+Sans:ital,wght@0,400;0,600;0,700;1,700&family=Oswald:wght@600&display=swap">
<style>
  :root {
    --blue: #1f5ea8;
    --blue-deep: #154b8c;
    --green: #8dc63f;
    --green-light: #a8d65a;
    --sky: #3b9ad9;
    --gold: #ae9a38;
    --brand-blue: #1d5fa8;
    --white: #ffffff;
    --ink: #2b2b2b;
  }
  * { margin: 0; padding: 0; box-sizing: border-box; }
  html, body { width: 971px; height: 1200px; overflow: hidden; background: #f2f2f2; }
  .flier {
    position: relative; width: 971px; height: 1200px; overflow: hidden;
    background: var(--blue); font-family: "Open Sans", sans-serif; color: var(--white);
  }
  .hero-photo {
    position: absolute; left: 0; top: 0; width: 971px; height: 667px;
    background: linear-gradient(110deg, #e9ebe8 0%, #c9c6bd 35%, #b4462f 62%, #8a3636 78%, #b9b2a5 100%);
  }
  .brand {
    position: absolute; left: 60px; top: 150px; display: flex; align-items: center; gap: 14px;
  }
  .brand-dot { width: 40px; height: 40px; border-radius: 50%; background: var(--brand-blue); }
  .brand-name { font-size: 30px; font-weight: 600; color: var(--brand-blue); }
  .nmls {
    position: absolute; left: 55px; top: 560px; font-size: 20px; font-weight: 700;
    text-shadow: 0 1px 3px rgba(0,0,0,.5);
  }
  .url-tab { position: absolute; left: 32px; top: 620px; width: 478px; height: 58px; }
  .url-text {
    position: absolute; left: 76px; top: 630px; font-size: 25px; font-weight: 700; letter-spacing: .3px;
    white-space: nowrap; text-shadow: 0 1px 2px rgba(0,0,0,.35);
  }
  .headline {
    position: absolute; left: 50px; top: 702px; font-family: "Oswald", sans-serif; font-weight: 600;
    font-size: 68px; line-height: 66px; text-transform: uppercase; white-space: nowrap;
    text-shadow: 0 2px 3px rgba(0,0,0,.3);
  }
  .badge {
    position: absolute; left: 662px; top: 537px; width: 252px; height: 252px; border-radius: 50%;
    background: var(--green); box-shadow: 0 6px 12px rgba(0,0,0,.35);
    display: flex; align-items: center; justify-content: center;
  }
  .badge-inner {
    width: 226px; height: 226px; border-radius: 50%;
    background: radial-gradient(circle at 50% 35%, #ffffff 55%, #dcdcdc 100%);
    display: flex; align-items: center; justify-content: center; text-align: center;
    color: var(--ink); font-weight: 600; font-size: 33px; line-height: 42px;
  }
  .programs { position: absolute; left: 52px; top: 858px; }
  .programs-lead { font-size: 23px; font-weight: 600; line-height: 30px; }
  .programs-sub { font-size: 17px; font-weight: 600; line-height: 24px; }
  .highlights { list-style: none; margin-top: 14px; }
  .highlights li { position: relative; padding-left: 28px; font-size: 18px; line-height: 29px; }
  .highlights svg { position: absolute; left: 0; top: 9px; width: 15px; height: 15px; }
  .divider {
    position: absolute; left: 532px; top: 880px; width: 2px; height: 200px;
    background: linear-gradient(to bottom, transparent, var(--blue-deep) 20%, var(--blue-deep) 80%, transparent);
  }
  .product-line { position: absolute; left: 576px; top: 855px; }
  .product-title { font-size: 28px; font-weight: 600; line-height: 37px; white-space: nowrap; }
  .product-contact { font-size: 23px; line-height: 33px; margin-top: 24px; }
  .product-contact em { font-weight: 700; }
  .product-phone { font-family: "Oswald", sans-serif; font-size: 38px; line-height: 50px; margin-top: 8px; }
  .footer-waves { position: absolute; left: 0; top: 1070px; width: 971px; height: 130px; }
  .footer-contact {
    position: absolute; left: 52px; top: 1140px; font-size: 20px; font-weight: 700; font-style: italic;
    white-space: nowrap;
  }
  .footer-contact .phone { font-family: "Oswald", sans-serif; font-style: normal; font-size: 31px; margin-left: 4px; }
  .footer-email {
    position: absolute; left: 576px; top: 1153px; font-size: 14px; font-weight: 700; white-space: nowrap;
  }
</style>
</head>
<body>
<div class="flier">
  <div class="hero-photo" role="img" aria-label="Photo of a smiling construction worker in a yellow hard hat and plaid shirt carrying lumber on his shoulder at a building site"></div>

  <div class="brand">
    <span class="brand-dot"></span>
    <span class="brand-name">Brightlane Funding, Inc.</span>
  </div>

  <div class="nmls">NMLS #731856</div>

  <svg class="url-tab" viewBox="0 0 478 58" aria-hidden="true">
    <path d="M0 58 L478 58 L460 6 Q458 0 445 0 L45 0 Q32 0 28 8 Z" fill="var(--green)"/>
  </svg>
  <div class="url-text">www.brightlanefunding.example</div>

  <h1 class="headline">Hard Money Fix<br>&amp; Flip Programs</h1>

  <div class="badge"><div class="badge-inner">Hard<br>Money Loan<br>Products<br>offered</div></div>

  <section class="programs">
    <p class="programs-lead">We offer a variety of loan programs</p>
    <p class="programs-sub">Some program highlights include......</p>
    <ul class="highlights">
      <li><svg viewBox="0 0 15 15"><rect x="1" y="3" width="11" height="11" fill="none" stroke="#fff" stroke-width="1.4"/><path d="M3 8 L6.5 11.5 L14 1.5" fill="none" stroke="#e6e22a" stroke-width="2.4"/></svg>No Minimum Credit Score</li>
      <li><svg viewBox="0 0 15 15"><rect x="1" y="3" width="11" height="11" fill="none" stroke="#fff" stroke-width="1.4"/><path d="M3 8 L6.5 11.5 L14 1.5" fill="none" stroke="#e6e22a" stroke-width="2.4"/></svg>3-5 Day Close</li>
      <li><svg viewBox="0 0 15 15"><rect x="1" y="3" width="11" height="11" fill="none" stroke="#fff" stroke-width="1.4"/><path d="M3 8 L6.5 11.5 L14 1.5" fill="none" stroke="#e6e22a" stroke-width="2.4"/></svg>Up to 100% of Purchase &amp; Rehab</li>
      <li><svg viewBox="0 0 15 15"><rect x="1" y="3" width="11" height="11" fill="none" stroke="#fff" stroke-width="1.4"/><path d="M3 8 L6.5 11.5 L14 1.5" fill="none" stroke="#e6e22a" stroke-width="2.4"/></svg>Rates as Low as 7%</li>
      <li><svg viewBox="0 0 15 15"><rect x="1" y="3" width="11" height="11" fill="none" stroke="#fff" stroke-width="1.4"/><path d="M3 8 L6.5 11.5 L14 1.5" fill="none" stroke="#e6e22a" stroke-width="2.4"/></svg>Loans Offered Nationwide</li>
    </ul>
  </section>

  <div class="divider"></div>

  <section class="product-line">
    <p class="product-title">Check Out Our Exciting<br>New Product Line</p>
    <p class="product-contact">Contact us today for more<br>information at: <em>Loan experts:</em></p>
    <p class="product-phone">800-647-2915</p>
  </section>

  <svg class="footer-waves" viewBox="0 0 971 130" preserveAspectRatio="none" aria-hidden="true">
    <path d="M0 50 Q100 24 230 20 Q110 32 0 58 Z" fill="var(--green-light)"/>
    <path d="M0 56 Q200 20 430 30 Q650 42 780 44 Q900 42 971 8 L971 24 Q880 62 700 62 Q400 58 0 70 Z" fill="var(--sky)"/>
    <path d="M560 40 Q800 50 971 0 L971 10 Q790 58 560 40 Z" fill="var(--green)"/>
    <path d="M0 66 Q300 48 560 62 Q800 72 971 24 L971 130 L0 130 Z" fill="var(--gold)"/>
  </svg>

  <div class="footer-contact">Contact us :<span class="phone">(800) 647-2915 x42</span></div>
  <div class="footer-email">email us at mwelton@brightlanefunding.example</div>
</div>
</body>
</html>
```